New Company Business Card Design

I have a new company logo and I want a new business card design. I dont know if the logo file i attached is in the correct format or quality. We are a New York City Specialty construction Firm specializing in high risk out of the box projects. I want a simple and classy business card that people will his card is as crisp as the work his company does.

Target Market(s)

Clients in the heavy construction industry in New York City

Industry/Entity Type

Construction Company

Contact Information for Business Card

Simple Classy - DIFFERENT

Font styles to use
Other font styles liked:
• Mach the logo font in some way

Colors

Designer to choose colors to be used in the design.

Requirements
Must have
• Uniqueness
Nice to have
• Nothing particular - Just different and classy - Timeless
Should not have
• Goofy Shit or Gimmicky shit

```html
<!DOCTYPE html>
<html lang="en">
<head>
<meta charset="utf-8">
<title>KRT Builders – Business Card</title>
<link rel="stylesheet" href="https://fonts.googleapis.com/css2?family=Roboto:wght@300;400;700&display=swap">
<style>
  :root {
    --page-bg: #e4e4e4;
    --card-white: #ffffff;
    --blue-light: #16b1ea;
    --blue-mid: #0a8ad8;
    --blue-deep: #0650a6;
    --brand-blue: #1a8fd8;
    --ink: #1b1b1b;
    --ink-soft: #3a3a3a;
    --tab-black: #111111;
    --back-dark: #1c1c1c;
    --back-mid: #2b2b2b;
    --back-line: #3a3a3a;
  }
  * { box-sizing: border-box; margin: 0; padding: 0; }
  html, body {
    width: 1200px; height: 800px; overflow: hidden;
    background: var(--page-bg);
    font-family: "Roboto", Arial, sans-serif;
  }
  .stage {
    position: relative; width: 1200px; height: 800px;
    display: flex; align-items: center; justify-content: center; gap: 60px;
  }
  .card {
    position: relative; width: 510px; height: 292px; overflow: hidden;
    box-shadow: 0 10px 28px rgba(0,0,0,.18);
  }

  /* Front */
  .card-front { background: var(--card-white); }
  .front-identity {
    position: absolute; left: 0; top: 0; width: 44%; height: 100%;
    padding: 58px 0 0 34px;
  }
  .brand-name {
    display: flex; align-items: center; gap: 8px;
    font-weight: 700; font-size: 25px; letter-spacing: .5px;
    color: var(--brand-blue); line-height: 1;
  }
  .brand-mark { width: 12px; height: 12px; background: var(--brand-blue); flex: none; }
  .brand-sub {
    margin-top: 6px; font-weight: 700; font-size: 10px; letter-spacing: 3px;
    color: var(--brand-blue);
  }
  .person-name { margin-top: 40px; font-size: 15px; color: var(--brand-blue); letter-spacing: 1px; }
  .person-phone { margin-top: 4px; font-size: 13px; color: var(--ink-soft); letter-spacing: 1px; }

  .front-contact {
    position: absolute; right: 0; top: 0; width: 56%; height: 100%;
    background: linear-gradient(160deg, var(--blue-light) 0%, var(--blue-mid) 45%, var(--blue-deep) 100%);
    padding-top: 40px;
  }
  .contact-list { list-style: none; }
  .contact-item {
    display: flex; align-items: center; gap: 16px;
    height: 30px; margin-bottom: 14px;
    font-size: 14px; font-weight: 300; color: var(--ink); letter-spacing: .4px;
  }
  .contact-icon {
    width: 30px; height: 30px; background: var(--tab-black);
    display: flex; align-items: center; justify-content: center; flex: none;
  }
  .contact-icon svg { width: 16px; height: 16px; fill: #fff; }

  /* Back */
  .card-back {
    background: linear-gradient(180deg, var(--back-mid) 0%, var(--back-dark) 100%);
  }
  .back-skyline {
    position: absolute; left: 0; right: 0; top: 0; height: 100%;
    background: linear-gradient(180deg, rgba(70,70,70,.35) 0%, rgba(40,40,40,.15) 60%, rgba(0,0,0,0) 100%);
  }
  .back-band {
    position: absolute; left: 0; right: 0; top: 36%; height: 1px; background: var(--back-line);
  }
  .back-logo {
    position: absolute; left: 50%; top: 50%; transform: translate(-50%, -50%);
    text-align: center;
  }
  .back-logo .brand-name { justify-content: center; font-size: 30px; }
</style>
</head>
<body>
<main class="stage">

  <section class="card card-front" aria-label="Business card front">
    <div class="front-identity">
      <div class="brand-name"><span class="brand-mark"></span>KRT</div>
      <div class="brand-sub">BUILDERS, INC.</div>
      <p class="person-name">XXXX XXXXXXX</p>
      <p class="person-phone">000000000</p>
    </div>
    <div class="front-contact">
      <ul class="contact-list">
        <li class="contact-item">
          <span class="contact-icon"><svg viewBox="0 0 24 24"><path d="M6.6 10.8a15 15 0 0 0 6.6 6.6l2.2-2.2c.3-.3.7-.4 1-.2 1.1.4 2.3.6 3.6.6.6 0 1 .4 1 1V20c0 .6-.4 1-1 1A17 17 0 0 1 3 4c0-.6.4-1 1-1h3.5c.6 0 1 .4 1 1 0 1.3.2 2.5.6 3.6.1.3 0 .7-.2 1z"/></svg></span>
          00000000000
        </li>
        <li class="contact-item">
          <span class="contact-icon"><svg viewBox="0 0 24 24"><path d="M3 5h18v14H3zm2 2v.5l7 4.5 7-4.5V7zm0 3v7h14v-7l-7 4.5z"/></svg></span>
          xxxxxxx@xxxxxxx.com
        </li>
        <li class="contact-item">
          <span class="contact-icon"><svg viewBox="0 0 24 24"><path d="M12 2a10 10 0 1 0 0 20 10 10 0 0 0 0-20zm6.9 6h-3a15 15 0 0 0-1.3-3.9A8 8 0 0 1 18.9 8zM12 4c.8 1.2 1.5 2.5 1.9 4h-3.8c.4-1.5 1.1-2.8 1.9-4zM4.3 14a8 8 0 0 1 0-4h3.4a16 16 0 0 0 0 4zm.8 2h3a15 15 0 0 0 1.3 3.9A8 8 0 0 1 5.1 16zm3-8h-3a8 8 0 0 1 4.3-3.9C8.8 5.3 8.4 6.6 8.1 8zM12 20c-.8-1.2-1.5-2.5-1.9-4h3.8c-.4 1.5-1.1 2.8-1.9 4zm2.3-6H9.7a14 14 0 0 1 0-4h4.6a14 14 0 0 1 0 4zm.3 5.9c.6-1.2 1-2.5 1.3-3.9h3a8 8 0 0 1-4.3 3.9zm1.7-5.9a16 16 0 0 0 0-4h3.4a8 8 0 0 1 0 4z"/></svg></span>
          www.xxxxxx.com
        </li>
        <li class="contact-item">
          <span class="contact-icon"><svg viewBox="0 0 24 24"><path d="M12 2a7 7 0 0 0-7 7c0 5.2 7 13 7 13s7-7.8 7-13a7 7 0 0 0-7-7zm0 9.5a2.5 2.5 0 1 1 0-5 2.5 2.5 0 0 1 0 5z"/></svg></span>
          xxxxxxx, xxxxxxxx, xxxx-123
        </li>
      </ul>
    </div>
  </section>

  <section class="card card-back" aria-label="Business card back">
    <div class="back-skyline" role="img" aria-label="Faint city skyline with construction cranes"></div>
    <div class="back-band"></div>
    <div class="back-logo">
      <div class="brand-name"><span class="brand-mark"></span>KRT</div>
      <div class="brand-sub">BUILDERS, INC.</div>
    </div>
  </section>

</main>
</body>
</html>
```